Business Card Design Project

We're an orthopaedic office, and our colors are blue white and balck. Dealing with physicians and healthcare execs, I'd like this card to have a classy, yet overpowering wow factor.

Here are a couple of cards I like that are close to what I'm looking for:
http://www.pixelbazaro.com/design/392047
http://www.pixelbazaro.com/design/286390

Industry/Entity Type

Healthcare

```html
<!DOCTYPE html>
<html lang="en">
<head>
<meta charset="utf-8">
<title>Graham Ellison — Business Card</title>
<link href="https://fonts.googleapis.com/css2?family=Didact+Gothic&display=swap" rel="stylesheet">
<style>
  :root {
    --card-black: #000000;
    --ink-white: #ffffff;
    --blue-deep: #1b3fae;
    --blue-mid: #2f6fe0;
    --blue-bright: #3aa6f2;
    --cyan-glow: #5fe3f5;
    --ice: #b9ecfb;
  }
  * { margin: 0; padding: 0; box-sizing: border-box; }
  html, body {
    width: 1200px;
    height: 693px;
    overflow: hidden;
    background: var(--card-black);
  }
  .card {
    position: relative;
    width: 1200px;
    height: 693px;
    background: var(--card-black);
    font-family: "Didact Gothic", sans-serif;
    color: var(--ink-white);
  }
  .wave-panel {
    position: absolute;
    left: 0;
    top: 0;
    width: 429px;
    height: 693px;
    background:
      radial-gradient(ellipse 60% 40% at 85% 60%, var(--cyan-glow) 0%, rgba(95,227,245,0) 70%),
      radial-gradient(ellipse 50% 30% at 30% 45%, var(--ice) 0%, rgba(185,236,251,0) 70%),
      linear-gradient(160deg, var(--blue-deep) 0%, var(--blue-mid) 35%, var(--blue-bright) 65%, var(--blue-mid) 100%);
  }
  .identity, .contact {
    position: absolute;
    right: 128px;
    text-align: right;
    line-height: 1;
  }
  .identity { top: 202px; }
  .identity .name {
    display: block;
    font-size: 63px;
    letter-spacing: 0.5px;
  }
  .identity .role {
    display: block;
    margin-top: 6px;
    font-size: 42px;
    font-style: italic;
  }
  .contact { top: 435px; }
  .contact .line {
    display: block;
    font-size: 31px;
    margin-bottom: 14px;
  }
</style>
</head>
<body>
  <div class="card">
    <div class="wave-panel" role="img" aria-label="Abstract flowing blue and cyan wave pattern"></div>
    <div class="identity">
      <span class="name">graham ellison</span>
      <span class="role">ceo</span>
    </div>
    <div class="contact">
      <span class="line address">2178 Lakeview Rd., Riverton, LA 70499</span>
      <span class="line phone">tel: 318.555.0142</span>
      <span class="line email">gellison@centralvalortho.com</span>
    </div>
  </div>
</body>
</html>
```